依頼詳細
依頼対象ページは「トップページ」と「アクティビティページ」になります。
※ワイヤーフレーム画像を添付いたします。参考にしてください。形状や表示位置等は必ずこの通りにしなければならないというものではありません。お任せいたします。
※利用可能なイメージを添付します。こちらもご利用下さい。

「トップページ」
・「アクティビティ画像群」は鳥沼村の観光スポットを一つずつ画像タイルにして表示させたいと考えています。
・新着情報内の画像は不要です。イメージがあればあてはめて頂いて構いません。
「アクティビティページ」
・「夏の千畳敷」と「投稿一覧」内の画像は不要です。イメージがあればあてはめて頂いて構いません。
・木曽駒ヶ岳だけでなく、その他のアクティビティページにも流用可能なデザインでお願いします。

■その他
・「トップページ」と「アクティビティページ」でヘッダーの大きさを変えて頂いても構いません
・希望色に関してオレンジまたは黒をベースを希望としています。どちらでも構いません。
・SEOを考慮したいのでデザイン内でテキストが可変となりそうな箇所はブラウザ(IE)のデフォルトフォントの使用をお願い致します。
サイトURL
http://www.vill.torinuma-ex.jp/kanko.php
ページ数
2ページ
希望イメージ
シンプル 複雑
単色 カラフル
暗い 明るい
日常 高級
遊び心 厳粛
未来的 伝統的
女性的 男性的
希望する色
オレンジベースまたは黒ベース
納品ファイル
• 高解像度JPG (.jpg)
• イラストレーター形式 (.ai)
補足説明
トップページの画像タイルは大タイル、中タイルの2種類で構成したいと考えています。
季節やイベントの有無によって入れ替えます。
タイル内の「子どもと楽しめるアイコン」「時間アイコン」「インフォメーションエリア」は
様々なアクティビティで共通で利用します。それぞれがの情報が分かりやすい形でデザインをお願いします。
遅くなりすみません。
写真素材は容量が大きいため、添付ではなく以下のURLよりダウンロードしてください。
お手数をお掛けしますが宜しくお願い致します。

■photo1
http://pakkubox-ex.jp/download/a19c3f0b72d84e6a95c1b0d7e3f28a4c6d90b1e2

■photo2
http://pakkubox-ex.jp/download/7c2e90d4b1a83f65e07d9c1b4a2f8e36d5b0c9a7

ワイヤーフレームの「アクティビティ」タイル内に入れる画像はそれぞれ該当する「楓原水産」や「中央アルプス」などを利用してください。
全体的なイメージとして利用するものはお任せいたします。
納品ファイルですがPSD、PNG等の形式でも構いません。
お任せいたします。
素材写真の同じものを下記ミラーサイトに配置しました。
こちらからDLしても構いません。

photo1:
http://survey.kawaridojo-ex.com/photo1.zip

photo2:
http://survey.kawaridojo-ex.com/photo2.zip
・アクティビティページの「カテゴリ」に関して
→すみません。「カテゴリ名」ではなく「アクティビティ名」となります。それぞれのアクティビティを取りまとめるようなカテゴリーの概念はありません。
ミラーサイトのzipファイルが壊れていたので差し替えました。
正常にDL、解凍できることを確認しております。

ご迷惑をおかけしすみませんでした。
締切を1日延ばします。

観光協会のスタッフの皆様にサイトリニューアルのコンセプトをお伝えしたうえで、一次投票、決選投票という手順を踏んで決定いたしました。

この度は多数のご応募ありがとうございました。観光協会の方も大変喜んでおられました。

```html
<!DOCTYPE html>
<html lang="ja">
<head>
<meta charset="utf-8">
<title>信州とりぬま観光ガイド</title>
<link href="https://fonts.googleapis.com/css2?family=Noto+Sans+JP:wght@400;700&family=Noto+Serif+JP:wght@700;900&display=swap" rel="stylesheet">
<style>
:root{
  --orange:#e8892b;
  --orange-dark:#c8661a;
  --beige:#f4efe4;
  --paper:#fbf8f1;
  --ink:#3b3128;
  --muted:#7a6e62;
  --line:#d9cfbf;
  --green:#5b8a3a;
  --sns:#3b5a98;
  --white:#fff;
}
*{box-sizing:border-box;margin:0;padding:0}
html,body{width:761px;height:1200px;overflow:hidden}
body{background:var(--beige);font-family:"Noto Sans JP",sans-serif;color:var(--ink);font-size:11px;position:relative}
.topbar{height:18px;padding:3px 22px;font-size:8px;color:var(--muted)}
.header{height:118px;position:relative;padding:10px 22px}
.site-title{font-family:"Noto Serif JP",serif;font-weight:900;color:var(--orange);font-size:40px;line-height:1.1;letter-spacing:1px}
.site-sub{font-family:"Noto Serif JP",serif;font-weight:700;color:var(--muted);font-size:13px;margin:4px 0 0 20px}
.header-link{position:absolute;right:24px;top:14px;font-size:8px;color:var(--muted)}
.tile{position:absolute;overflow:hidden;border:3px solid var(--white);box-shadow:0 1px 3px rgba(0,0,0,.2)}
.photo{position:absolute;inset:0}
.tile-big{left:24px;top:140px;width:712px;height:240px}
.tile-big .photo{background:linear-gradient(135deg,#6f8a4a 0%,#a7b27a 40%,#8a7d5d 70%,#54633a 100%)}
.tile-label{position:absolute;left:12px;top:10px;background:rgba(255,255,255,.88);padding:6px 14px 8px;border-radius:3px}
.tile-label small{display:block;font-size:10px;color:var(--green);font-weight:700}
.tile-label strong{font-family:"Noto Serif JP",serif;font-size:32px;color:var(--ink);letter-spacing:2px}
.duration{position:absolute;width:62px;height:62px;border-radius:50%;background:var(--orange);color:var(--white);text-align:center;font-size:9px;font-weight:700;padding-top:9px;line-height:1.2;border:2px solid var(--white)}
.duration b{display:block;font-size:24px;line-height:1}
.duration b span{font-size:10px}
.info{position:absolute;background:rgba(255,255,255,.92);font-size:9px;border-radius:3px;padding:5px 7px;border-collapse:separate}
.info td{padding:2px 3px}
.info th{background:var(--orange);color:var(--white);font-weight:700;padding:2px 5px;border-radius:2px;white-space:nowrap}
.tile-mid{top:390px;width:350px;height:205px}
.tile-fest{left:24px}
.tile-fest .photo{background:linear-gradient(160deg,#4f7d3a 0%,#8db05f 50%,#d9d2b8 100%)}
.tile-peak{left:386px}
.tile-peak .photo{background:linear-gradient(180deg,#5c8fc4 0%,#a9c6e0 40%,#7f8a6e 75%,#56663f 100%)}
.tile-mid .tile-label strong{font-size:24px}
.more{position:absolute;right:26px;top:601px;font-size:9px;color:var(--muted)}
.news{position:absolute;left:24px;top:620px;width:446px;background:var(--paper);border:1px solid var(--line)}
.news h2{font-size:15px;color:var(--orange-dark);padding:6px 10px;border-bottom:2px solid var(--orange)}
.news-item{display:flex;gap:10px;padding:10px;border-bottom:1px dashed var(--line);height:108px}
.thumb{width:100px;height:76px;flex:none}
.news-item time{display:block;font-size:9px;color:var(--orange-dark);font-weight:700}
.news-item h3{font-size:10px;color:#2c5a9c;margin:2px 0 4px}
.news-item p{font-size:9px;line-height:1.6;color:var(--muted)}
.news-item .detail{display:block;text-align:right;font-size:8px;margin-top:4px}
.news-foot{font-size:8px;text-align:right;padding:6px 10px;color:var(--muted)}
.side{position:absolute;left:482px;top:620px;width:254px}
.sns-box{background:var(--sns);color:var(--white);padding:6px 10px;height:90px}
.sns-box .tag{font-size:9px;background:rgba(255,255,255,.2);padding:2px 5px;display:inline-block}
.sns-name{display:flex;align-items:center;gap:8px;margin-top:12px;font-size:15px;font-weight:700;line-height:1.3}
.sns-name i{width:30px;height:30px;background:var(--white);flex:none}
.side-link{display:flex;align-items:center;gap:10px;background:var(--paper);border:1px solid var(--line);height:60px;margin-top:10px;padding:0 12px;font-size:13px;font-weight:700;color:var(--ink)}
.side-link svg{width:28px;height:28px}
.pagetop{position:absolute;right:26px;top:1010px;font-size:8px;color:var(--muted)}
.footer{position:absolute;left:0;top:1030px;width:761px;height:170px;background:var(--orange);color:var(--white);border-top:4px solid var(--orange-dark)}
.footer-inner{padding:18px 24px 0}
.footer h2{font-family:"Noto Serif JP",serif;font-size:28px;letter-spacing:3px;margin-bottom:4px}
.footer p{font-size:10px;line-height:1.7}
.copyright{position:absolute;bottom:8px;width:100%;text-align:center;font-size:8px}
</style>
</head>
<body>
<div class="topbar">鳥沼村観光協会 ｜ 信州鳥沼の観光情報サイト</div>
<header class="header">
  <div class="site-title">信州とりぬま観光ガイド</div>
  <div class="site-sub">〜駒ヶ岳麓とくつろぎの里〜</div>
  <div class="header-link">鳥沼村観光協会ホームページ</div>
</header>

<section class="tile tile-big">
  <div class="photo" role="img" aria-label="釣り堀で家族が魚を釣って楽しむ写真"></div>
  <div class="tile-label"><small>レジャーの前の釣り堀・バーベキュー</small><strong>楓原水産</strong></div>
  <div class="duration" style="right:20px;top:70px">所要時間<b>30<span>分</span></b></div>
  <table class="info" style="right:20px;top:150px">
    <tr><th>営業時間</th><td>朝9時〜夜6時</td></tr>
    <tr><th>営業期間</th><td>通年</td></tr>
    <tr><th>オススメ期間</th><td>6月〜9月</td></tr>
  </table>
</section>

<section class="tile tile-mid tile-fest">
  <div class="photo" role="img" aria-label="夏祭りで踊る人々の写真"></div>
  <div class="tile-label"><small>夏の恒例行事</small><strong>鳥沼おどり祭</strong></div>
  <table class="info" style="right:10px;bottom:10px">
    <tr><th>日付</th><td>7月20日(土)</td></tr>
    <tr><th>時間</th><td>夕方4時〜夜11時頃</td></tr>
  </table>
</section>

<section class="tile tile-mid tile-peak">
  <div class="photo" role="img" aria-label="中央アルプスの山並みと高山植物の写真"></div>
  <div class="tile-label"><small>中央アルプス・千畳敷</small><strong>木曽駒ヶ岳</strong></div>
  <div class="duration" style="left:14px;top:110px">所要時間<b>4<span>時間</span></b></div>
  <table class="info" style="right:10px;bottom:10px">
    <tr><th>運行期間</th><td>4月〜11月</td></tr>
    <tr><th>オススメ期間</th><td>7月〜9月</td></tr>
  </table>
</section>
<div class="more">一覧を見る ▶</div>

<section class="news">
  <h2>新着情報</h2>
  <article class="news-item">
    <div class="thumb" role="img" aria-label="高原キャンプ場の写真" style="background:linear-gradient(135deg,#5d7f45,#a9c08a)"></div>
    <div><time>2013年6月21日</time><h3>鳥沼高原キャンプ場のお知らせについて【文書】</h3><p>鳥沼高原キャンプ場の開場についてお知らせします。ご利用の際は事前にお申し込みください。</p><span class="detail">続きを見る ▶</span></div>
  </article>
  <article class="news-item">
    <div class="thumb" role="img" aria-label="町並みの建物の写真" style="background:linear-gradient(135deg,#8fa3b8,#d8d2c4)"></div>
    <div><time>2013年6月19日</time><h3>「信州鳥沼のトーチソフト」が名所地域賞を受賞【北の新聞】</h3><p>北の新聞社「信州鳥沼のトーチソフト」が第3回名所地域賞を受賞しました。</p><span class="detail">続きを見る ▶</span></div>
  </article>
  <article class="news-item">
    <div class="thumb" role="img" aria-label="店舗の外観写真" style="background:linear-gradient(135deg,#b7a47c,#e6dcc4)"></div>
    <div><time>2013年6月19日</time><h3>「信州鳥沼のトーチソフト」が名所地域賞を受賞【北の新聞】</h3><p>地域の名物として多くの方に親しまれています。今後ともよろしくお願いします。</p><span class="detail">続きを見る ▶</span></div>
  </article>
  <div class="news-foot">新着情報をもっと見る ▶</div>
</section>

<aside class="side">
  <div class="sns-box">
    <span class="tag">ソーシャルで最新情報を配信しています！</span>
    <div class="sns-name"><i></i><span>信州とりぬま観光協会<br>公式ソーシャルページ</span></div>
  </div>
  <a class="side-link"><svg viewBox="0 0 28 28"><circle cx="14" cy="14" r="12" fill="none" stroke="#e8892b" stroke-width="2"/><text x="14" y="19" text-anchor="middle" font-size="14" font-weight="700" fill="#e8892b">?</text></svg>よくあるご質問</a>
  <a class="side-link"><svg viewBox="0 0 28 28"><rect x="3" y="7" width="22" height="15" fill="none" stroke="#e8892b" stroke-width="2"/><path d="M3 7l11 8 11-8" fill="none" stroke="#e8892b" stroke-width="2"/></svg>お問い合せ</a>
</aside>
<div class="pagetop">▲ ページトップへ</div>

<footer class="footer">
  <div class="footer-inner">
    <h2>鳥沼村観光協会</h2>
    <p>〒399-0000 長野県上伊那郡鳥沼村100番地（鳥沼村役場 産業観光課内）</p>
    <p>TEL 0265-00-1234　FAX 0265-00-1235</p>
    <p>E-mail info@torinuma-kanko.example　受付時間 平日8時30分〜17時15分</p>
  </div>
  <div class="copyright">© 鳥沼村観光協会</div>
</footer>
</body>
</html>
```